Electrical Business Card Design

New electrical business targeting my local area
Installations
Repairs
Switchboards
TV / Vistacast / Antennas
Telephone
Data Networks
Audio Visual
Licence # 518427K
ABN 58316927405
I would like some white background, black writing, red, blue & green can be used
Designer discretion to be used on layout, colour placement & any images
Reason: To give designers more time, I thought 5 days wasn't enough
Please don't just create generic business cards................include personal details e.g. business name, contact name, ph #, email. Also include the things I do, licence # & abn (refer to brief for all details)
Thanks
Reason: Would like more designs & have now committed my payment, thank you
Industry/Entity Type
Electrical
Contact Information for Business Card
Korvane Electrical Services,
Gareth Pelling,
0438 571 963,
korvaneelectrical@wexmail.net.au,
My suburb is Tarlow
Look and feel

```html
<!DOCTYPE html>
<html lang="en">
<head>
<meta charset="utf-8">
<title>Korvane Electrical Services – Business Card</title>
<link rel="stylesheet" href="https://fonts.googleapis.com/css2?family=Cabin:wght@400;500&family=Caladea:wght@700&display=swap">
<style>
  :root {
    --red: #c8202a;
    --pink-soft: #f6d9cf;
    --pink-mid: #e59a86;
    --grey-text: #555555;
    --ink: #1e1e1e;
    --card: #ffffff;
    --stage: #ecebea;
  }
  * { margin: 0; padding: 0; box-sizing: border-box; }
  html, body { width: 1200px; height: 922px; overflow: hidden; background: var(--stage); }
  body { position: relative; font-family: "Cabin", sans-serif; }

  .card {
    position: absolute;
    width: 684px;
    height: 414px;
    background: var(--card);
    border-radius: 14px;
    overflow: hidden;
    box-shadow: 0 1px 3px rgba(0,0,0,0.12);
  }
  .card--back { left: 400px; top: 88px; }
  .card--front { left: 116px; top: 430px; }

  /* back side */
  .services-tab {
    position: absolute; left: 0; top: 40px; width: 174px; height: 34px;
    background: var(--red); border-radius: 0 17px 17px 0;
    color: #fff; font-family: "Caladea", serif; font-weight: 700; font-size: 19px;
    line-height: 34px; padding-left: 38px;
  }
  .edge-tab {
    position: absolute; right: 0; width: 34px; background: var(--red);
    border-radius: 17px 0 0 17px;
  }
  .card--back .edge-tab { top: 40px; height: 34px; }
  .services-list {
    position: absolute; left: 38px; top: 86px; list-style: none;
    font-size: 12px; color: var(--ink);
  }
  .services-list li { height: 32px; display: flex; align-items: flex-start; }
  .services-list li::before {
    content: ""; width: 5px; height: 5px; background: var(--red);
    margin: 4px 8px 0 0; flex: none;
  }
  .pixel-field {
    position: absolute;
    background: radial-gradient(ellipse at center, var(--pink-mid) 0%, var(--pink-soft) 55%, rgba(255,255,255,0) 75%);
    opacity: 0.75;
  }
  .card--back .pixel-field { left: 462px; top: 66px; width: 212px; height: 280px; }
  .credentials {
    position: absolute; right: 17px; top: 386px;
    font-size: 10px; color: var(--ink);
  }

  /* front side */
  .brand-band {
    position: absolute; left: 0; top: 172px; width: 392px; height: 39px;
    background: var(--red); border-radius: 0 19px 19px 0;
    display: flex; align-items: center; padding-left: 34px; gap: 14px;
  }
  .brand-mark {
    width: 30px; height: 30px; border-radius: 50%;
    border: 2px solid #fff; flex: none;
  }
  .brand-name { color: #fff; font-size: 24px; font-weight: 400; white-space: nowrap; }
  .tagline {
    position: absolute; left: 240px; top: 216px;
    font-size: 17px; color: var(--grey-text);
  }
  .card--front .edge-tab { top: 172px; height: 39px; border-radius: 19px 0 0 19px; }
  .contact {
    position: absolute; right: 44px; top: 156px; text-align: right;
    color: var(--red); font-size: 15px; line-height: 24.5px; font-style: normal;
    white-space: nowrap;
  }
  .card--front .pixel-field {
    left: 6px; top: 240px; width: 672px; height: 156px;
    background: linear-gradient(90deg, rgba(255,255,255,0), var(--pink-soft) 8%, var(--pink-mid) 30%, var(--pink-soft) 50%, var(--pink-mid) 75%, var(--pink-soft) 92%, rgba(255,255,255,0));
    opacity: 0.55;
    border-radius: 40px;
  }
</style>
</head>
<body>

  <section class="card card--back" aria-label="Card reverse">
    <div class="services-tab">'Things I do' -</div>
    <div class="edge-tab"></div>
    <ul class="services-list">
      <li>New installations</li>
      <li>Repairs &amp; additions</li>
      <li>TV/Vistacast/Antennas</li>
      <li>Phones</li>
      <li>Data Networks</li>
      <li>Audio Visual</li>
    </ul>
    <div class="pixel-field" role="img" aria-label="Scattered red and pink pixel-square pattern"></div>
    <p class="credentials">Licence # 518427K &nbsp;|&nbsp; ABN 58316927405</p>
  </section>

  <section class="card card--front" aria-label="Card front">
    <div class="brand-band">
      <span class="brand-mark"></span>
      <span class="brand-name">Korvane Electrical Services</span>
    </div>
    <p class="tagline">Reliable &amp; Honest</p>
    <div class="edge-tab"></div>
    <address class="contact">
      Gareth Pelling<br>
      0438 571 963<br>
      korvane@wexmail.net.au Tarlow
    </address>
    <div class="pixel-field" role="img" aria-label="Band of red and pink pixel squares running across the card"></div>
  </section>

</body>
</html>
```